Tavenorix - world unique technology for better life - please let them know who am i at first sight

We need a new business card for company which is a provider of unique crystal based technology suitable for all living being. For more information and final design you can use our brochure (our colours are black and blue from brochure).
We use Verdana font

Industry/Entity Type

Business

Contact Information for Business Card

regular dimension

Font styles to use
Other font styles liked:
• Verdana

Requirements
Must have
• Logo
• name
• function/position
• phone
• mobile
• e-mail
• adress
Nice to have
• inovative design (technology directed)

```html
<!DOCTYPE html>
<html lang="en">
<head>
<meta charset="utf-8">
<title>Tavenorix – Business Card</title>
<link href="https://fonts.googleapis.com/css2?family=Noto+Sans:wght@300;400;700&display=swap" rel="stylesheet">
<style>
  :root {
    --stage: #cfcb9c;
    --card: #000000;
    --blue: #1e9ad6;
    --white: #ffffff;
    --slate: #3b4d59;
    --slate-deep: #1a252c;
  }
  * { margin: 0; padding: 0; box-sizing: border-box; }
  html, body { width: 1200px; height: 394px; overflow: hidden; background: var(--stage); }
  body { position: relative; font-family: "Noto Sans", Verdana, sans-serif; }

  .card {
    position: absolute;
    top: 39px;
    width: 552px;
    height: 316px;
    background: var(--card);
    overflow: hidden;
  }
  .card--front { left: 21px; }
  .card--back { left: 610px; }

  .crystal-motif {
    position: absolute;
    top: 0;
    width: 162px;
    height: 316px;
    background: radial-gradient(ellipse at center, var(--slate) 0%, var(--slate-deep) 65%, var(--card) 100%);
  }
  .card--front .crystal-motif { right: 0; }
  .card--back .crystal-motif { left: 0; }

  .holder-name {
    position: absolute;
    left: 25px;
    top: 44px;
    font-size: 24px;
    font-weight: 700;
    color: var(--blue);
    letter-spacing: 0.3px;
  }
  .holder-role {
    position: absolute;
    left: 25px;
    top: 78px;
    font-size: 18.5px;
    font-weight: 400;
    color: var(--white);
  }

  .contact-list {
    position: absolute;
    left: 25px;
    top: 134px;
    list-style: none;
  }
  .contact-item {
    display: flex;
    align-items: center;
    height: 29.5px;
    font-size: 16px;
    color: var(--white);
  }
  .contact-icon {
    width: 16px;
    height: 16px;
    margin-right: 9px;
    flex: none;
  }

  .address {
    position: absolute;
    left: 25px;
    top: 297px;
    font-size: 13.5px;
    color: var(--white);
  }

  .brand-name {
    position: absolute;
    left: 186px;
    top: 112px;
    font-size: 60px;
    font-weight: 300;
    color: var(--blue);
    letter-spacing: 1px;
    line-height: 1;
  }
</style>
</head>
<body>

  <section class="card card--front">
    <div class="crystal-motif" role="img" aria-label="Decorative crystal lattice pattern"></div>

    <p class="holder-name">Mirela Kovanic</p>
    <p class="holder-role">Founder and CEO</p>

    <ul class="contact-list">
      <li class="contact-item">
        <svg class="contact-icon" viewBox="0 0 16 16" aria-hidden="true">
          <circle cx="8" cy="8" r="8" fill="var(--blue)"/>
          <path d="M5 4.5 L6.6 4.2 L7.3 6.2 L6.3 7 Q7 8.8 8.9 9.8 L9.8 8.8 L11.7 9.5 L11.5 11.2 Q7.5 11.5 5.2 8 Q4.4 6.2 5 4.5 Z" fill="var(--card)"/>
        </svg>
        012-345-6789
      </li>
      <li class="contact-item">
        <svg class="contact-icon" viewBox="0 0 16 16" aria-hidden="true">
          <rect x="4" y="1" width="8" height="14" rx="1.5" fill="var(--blue)"/>
          <rect x="5.3" y="3" width="5.4" height="5" fill="var(--card)"/>
          <circle cx="8" cy="11.8" r="1.1" fill="var(--card)"/>
        </svg>
        012-345-6789
      </li>
      <li class="contact-item">
        <svg class="contact-icon" viewBox="0 0 16 16" aria-hidden="true">
          <rect x="1" y="4" width="14" height="10" rx="1" fill="var(--blue)"/>
          <path d="M1.5 4.5 L8 9.5 L14.5 4.5" fill="none" stroke="var(--card)" stroke-width="1.3"/>
        </svg>
        info@tavenorix.com
      </li>
      <li class="contact-item">
        <svg class="contact-icon" viewBox="0 0 16 16" aria-hidden="true">
          <circle cx="8" cy="8" r="7.5" fill="var(--blue)"/>
          <g fill="none" stroke="var(--card)" stroke-width="0.9">
            <ellipse cx="8" cy="8" rx="3" ry="7"/>
            <line x1="1" y1="8" x2="15" y2="8"/>
            <path d="M2.2 4.5 H13.8 M2.2 11.5 H13.8"/>
          </g>
        </svg>
        www.tavenorix.cu
      </li>
    </ul>

    <p class="address">Street Name, City Name, Zipcode-01234</p>
  </section>

  <section class="card card--back">
    <div class="crystal-motif" role="img" aria-label="Decorative crystal lattice pattern"></div>
    <p class="brand-name">TAVENORIX</p>
  </section>

</body>
</html>
```